Little Forks, Calm Tables Book Cover

I'm looking for both an e-book and print cover for my upcoming book: Little Forks, Calm Tables: 8 Gentle Habits to for Changing How Your Kid Sees Every Meal. I prefer a simple design that communicates a family or child's peaceful relatinship with food. The book is authored by Lorinda Vaskel, MS, RD

Target Market(s)

Parents of young children

Colors
f04a50

Requirements
Nice to have
• I like simple covers with white and bright(ish) colors like red/green but am open to ideas from the designer. I also want the title to be easy to read.

```html
<!DOCTYPE html>
<html lang="en">
<head>
<meta charset="utf-8">
<title>Little Forks, Calm Tables — Book Cover</title>
<link rel="stylesheet" href="https://fonts.googleapis.com/css2?family=Merriweather:wght@300;400;700&family=Arimo:ital@1&display=swap">
<style>
  :root {
    --brand-red: #ec4b51;
    --paper: #f3f3f3;
    --paper-edge: #e9e9e9;
    --ink: #1f1f1f;
    --white: #ffffff;
  }
  * { margin: 0; padding: 0; box-sizing: border-box; }
  html, body { width: 1200px; height: 779px; overflow: hidden; background: var(--white); }
  .cover-spread { position: relative; width: 1200px; height: 779px; overflow: hidden; }

  .back-cover {
    position: absolute; left: 0; top: 0; width: 566px; height: 779px;
    background: var(--brand-red);
  }
  .back-blurb {
    position: absolute; left: 104px; top: 84px; width: 352px;
    font-family: "Merriweather", serif; font-weight: 400;
    font-size: 14.6px; line-height: 17.7px; color: var(--white);
  }
  .back-blurb p + p { margin-top: 17.7px; }
  .back-food {
    position: absolute; left: 201px; top: 581px; width: 123px; height: 129px;
    border-radius: 10px;
    background: radial-gradient(ellipse at 50% 50%, #eef1ea 0%, #dfe6d6 50%, #c9d4b8 75%, #8a6a4a 100%);
  }

  .spine {
    position: absolute; left: 566px; top: 0; width: 84px; height: 779px;
    background: linear-gradient(90deg, var(--paper-edge), var(--paper));
  }
  .spine-title, .spine-author {
    position: absolute; left: 50%; transform: translateX(-50%);
    writing-mode: vertical-rl; white-space: nowrap;
  }
  .spine-title {
    top: 90px; font-family: "Arimo", sans-serif; font-style: italic;
    font-size: 35px; line-height: 1; color: var(--brand-red);
  }
  .spine-author {
    top: 504px; font-family: "Merriweather", serif; font-weight: 400;
    font-size: 16px; line-height: 1; color: var(--ink);
  }

  .front-cover {
    position: absolute; left: 650px; top: 0; width: 550px; height: 779px;
    background: linear-gradient(180deg, #f6f6f6, #efefef);
    text-align: center;
  }
  .front-title {
    position: absolute; left: 0; right: 0; top: 50px;
    font-family: "Merriweather", serif; font-weight: 700; color: var(--brand-red);
    line-height: 1.12;
  }
  .front-title .line-small { display: block; font-size: 38px; }
  .front-title .line-large { display: block; font-size: 52px; }
  .front-subtitle {
    position: absolute; left: 0; right: 0; top: 168px;
    font-family: "Merriweather", serif; font-weight: 400;
    font-size: 18px; line-height: 26px; color: var(--ink);
  }
  .place-setting {
    position: absolute; left: 40px; top: 272px; width: 470px; height: 370px;
    background:
      radial-gradient(circle 182px at 50% 52%, #ffffff 0, #fbfbfb 150px, #f1f1f1 172px, #dedede 180px, rgba(230,230,230,0) 196px),
      radial-gradient(ellipse 12px 150px at 5% 50%, #d2d2d2 0, rgba(210,210,210,0) 100%),
      radial-gradient(ellipse 10px 170px at 96% 50%, #d2d2d2 0, rgba(210,210,210,0) 100%);
  }
  .front-author {
    position: absolute; left: 0; right: 0; top: 692px;
    font-family: "Merriweather", serif; font-weight: 700;
    font-size: 19px; color: var(--ink);
  }
</style>
</head>
<body>
<main class="cover-spread">
  <section class="back-cover">
    <div class="back-blurb">
      <p>Lorem ipsum dolor sit amet, consectetur adipiscing elit. Mauris ac odio ex. In a egestas lectus, fermentum congue tellus. Phasellus ligula mi, consequat quis consequat non, semper sed libero. Suspendisse elementum, metus a faucibus interdum, eros sapien posuere eros, ac molestie dolor augue sed erat. Phasellus nec urna tempor, bibendum magna vitae, luctus felis. Nulla arcu sem, tristique id pulvinar eget, egestas nec metus. Suspendisse ac hendrerit felis, at molestie ex. Vivamus vestibulum vestibulum libero vitae mollis. Donec pulvinar nisi nec malesuada porta. Aliquam nunc ligula, fringilla ut auctor vel, sodales eget sapien. Proin justo mi, consequat sit amet risus sed, fermentum maximus risus. Nulla vulputate nibh varius faucibus pellentesque. Aliquam varius sapien id pulvinar molestie.</p>
      <p>Donec dictum, tellus a tempus ultricies, nulla urna mollis dolor, in efficitur neque odio et dui. Sed luctus gravida diam, ut faucibus magna volutpat eget. Phasellus condimentum vestibulum turpis ut rutrum. Duis a massa quis arcu volutpat rhoncus id eget purus. In nisl dolor, malesuada a tellus et, fermentum</p>
    </div>
    <div class="back-food" role="img" aria-label="Slice of toast topped with cream cheese, cucumber and radish slices"></div>
  </section>

  <section class="spine">
    <div class="spine-title">Little Forks, Calm Tables</div>
    <div class="spine-author">Lorinda Vaskel, MS, RD</div>
  </section>

  <section class="front-cover">
    <h1 class="front-title">
      <span class="line-small">Little Forks,</span>
      <span class="line-large">Calm Tables</span>
    </h1>
    <p class="front-subtitle">8 Gentle Habits to for Changing How<br>Your Kid Sees Every Meal</p>
    <div class="place-setting" role="img" aria-label="White dinner plate with fruit, a treat and peas arranged playfully, set between a fork and a knife"></div>
    <p class="front-author">Lorinda Vaskel, MS, RD</p>
  </section>
</main>
</body>
</html>
```